Android Game Graphics
Puzzle Game Buttons/Background
I'm developing a puzzle game for android and I need a fun/colorful background and several buttons. I have attached sketches of the three screens I need graphics for.
The winning logo must "pop" like the "fuzzy otters" graphics. The graphics need to be fun and colorful, but I have no formal requirements. The game is a clone of the classic game "Glyphwalk". You can see/play the original game here: http://marlowjpenfield.com/android/games/glyphwalk.swf Below I have sketches of the three screens in the game, please make these with colorful graphics and buttons. For the first and second images, make sure the background image has "Quill Quest" somewhere spanning the back. For the third image, the one with the letters, make all of the letters/tiles the same color. Wood color like tilzor would probably be the best, but I'm open to suggestions. Also where "Quill Quest" is on the third image, make some sort of cartoony logo. I was thinking maybe the word formed from some sort of cartoony worm with glasses, but again, it's up to you. Please make all of the buttons, including the letters individually and high res because they will eventually be used on a 10 inch (1280 x 800 resolution tablet). Screen 1: http://img811.pixelcrate.net/i/introscreen1.png/ Screen 2: http://img827.pixelcrate.net/i/selectgame2.png/ Screen 3: http://img573.pixelcrate.net/i/gameplay3.png/ Basically, make the three images above how you think the game and menu should look. The resolution in the attached images is 854 x 480, but make sure you make them for a higher res tablet.

```html
<!DOCTYPE html>
<html lang="en">
<head>
<meta charset="utf-8">
<title>Quill Quest – Gameplay</title>
<link rel="stylesheet" href="https://fonts.googleapis.com/css2?family=Arimo:wght@400;700&display=swap">
<style>
  :root {
    --bg-light: #ffffff;
    --bg-mid: #c9c9c9;
    --bg-dark: #8e8e8e;
    --title-grey: #8a8a8a;
    --tile-light: #fbc27e;
    --tile-mid: #f39a38;
    --tile-dark: #d9700f;
    --tile-edge: #6b3a0a;
    --ink: #111111;
    --accent: #f07f14;
    --panel-light: #f2f2f2;
    --panel-mid: #bdbdbd;
    --panel-dark: #6f6f6f;
    --text-dark: #3a3a3a;
    --button-black: #111111;
    --worm-light: #d8a56a;
    --worm-dark: #8a5a2b;
  }
  * { box-sizing: border-box; margin: 0; padding: 0; }
  html, body { width: 1200px; height: 751px; overflow: hidden; }
  body {
    font-family: "Arimo", Arial, sans-serif;
    background: linear-gradient(160deg, var(--bg-light) 0%, var(--bg-mid) 45%, var(--bg-dark) 100%);
    position: relative;
  }
  .mascot {
    position: absolute;
    background: radial-gradient(ellipse at 40% 40%, var(--worm-light), var(--worm-dark));
  }
  .mascot--banner { left: 24px; top: 10px; width: 440px; height: 110px; border-radius: 55px; }
  .mascot--corner { left: 950px; top: 14px; width: 236px; height: 212px; border-radius: 50% 50% 45% 55%; }
  .game-title {
    position: absolute;
    left: 482px; top: 18px;
    font-size: 84px;
    font-weight: 400;
    color: var(--title-grey);
    letter-spacing: 1px;
    line-height: 1;
    white-space: nowrap;
  }
  .board {
    position: absolute;
    left: 12px; top: 137px;
    display: flex;
    gap: 0.5px;
  }
  .tile-column { display: flex; flex-direction: column; width: 83px; }
  .tile-column--low { margin-top: 48px; }
  .tile {
    position: relative;
    width: 83px; height: 92px;
    background: radial-gradient(circle at 50% 45%, var(--tile-light) 0%, var(--tile-mid) 55%, var(--tile-dark) 100%);
    border: 2px solid var(--tile-edge);
    display: flex; align-items: center; justify-content: center;
    font-weight: 700;
    font-size: 46px;
    color: var(--ink);
  }
  .tile__points {
    position: absolute;
    right: 6px; bottom: 4px;
    font-size: 18px;
  }
  .side-panel { position: absolute; left: 937px; top: 243px; width: 258px; }
  .stat {
    position: absolute; left: 0; width: 258px;
    display: flex; align-items: center; justify-content: center;
    font-weight: 700;
    border: 2px solid var(--panel-dark);
    white-space: nowrap;
  }
  .stat--score {
    top: 0; height: 76px; font-size: 40px; color: var(--text-dark);
    background: linear-gradient(var(--panel-light), var(--panel-mid));
  }
  .stat--word {
    top: 93px; height: 60px; font-size: 26px; color: #fff;
    background: linear-gradient(#f7a448, var(--accent));
  }
  .stat--points {
    top: 165px; height: 50px; font-size: 25px; color: #fff;
    background: linear-gradient(#d6d6d6, #8f8f8f);
  }
  .stat--level {
    top: 225px; height: 60px; font-size: 36px; color: var(--text-dark);
    background: linear-gradient(var(--panel-light), #a9a9a9);
  }
  .action {
    position: absolute;
    background: linear-gradient(#3a3a3a, var(--button-black) 50%);
    border: 2px solid #8c8c8c;
    border-radius: 8px;
    color: var(--accent);
    display: flex; align-items: center; justify-content: center;
    white-space: nowrap;
  }
  .action--clear { left: 0; top: 295px; width: 122px; height: 105px; font-size: 22px; }
  .action--scramble { left: 131px; top: 295px; width: 127px; height: 105px; font-size: 20px; }
  .action--submit { left: 0; top: 405px; width: 258px; height: 96px; font-size: 44px; border-radius: 12px; }
</style>
</head>
<body>
  <div class="mascot mascot--banner" role="img" aria-label="Cartoon worm stretched across the header"></div>
  <h1 class="game-title">quill quest</h1>
  <div class="mascot mascot--corner" role="img" aria-label="Cartoon worm mascot peeking in from the corner"></div>

  <main class="board">
    <div class="tile-column"><div class="tile">A<span class="tile__points">1</span></div><div class="tile">K<span class="tile__points">5</span></div><div class="tile">U<span class="tile__points">1</span></div><div class="tile">E<span class="tile__points">1</span></div><div class="tile">O<span class="tile__points">1</span></div><div class="tile">Y<span class="tile__points">4</span></div></div>
    <div class="tile-column tile-column--low"><div class="tile">A<span class="tile__points">1</span></div><div class="tile">K<span class="tile__points">5</span></div><div class="tile">U<span class="tile__points">1</span></div><div class="tile">E<span class="tile__points">1</span></div><div class="tile">O<span class="tile__points">1</span></div><div class="tile">Y<span class="tile__points">4</span></div></div>
    <div class="tile-column"><div class="tile">A<span class="tile__points">1</span></div><div class="tile">K<span class="tile__points">5</span></div><div class="tile">U<span class="tile__points">1</span></div><div class="tile">E<span class="tile__points">1</span></div><div class="tile">O<span class="tile__points">1</span></div><div class="tile">Y<span class="tile__points">4</span></div></div>
    <div class="tile-column tile-column--low"><div class="tile">A<span class="tile__points">1</span></div><div class="tile">K<span class="tile__points">5</span></div><div class="tile">U<span class="tile__points">1</span></div><div class="tile">E<span class="tile__points">1</span></div><div class="tile">O<span class="tile__points">1</span></div><div class="tile">Y<span class="tile__points">4</span></div></div>
    <div class="tile-column"><div class="tile">A<span class="tile__points">1</span></div><div class="tile">K<span class="tile__points">5</span></div><div class="tile">U<span class="tile__points">1</span></div><div class="tile">E<span class="tile__points">1</span></div><div class="tile">O<span class="tile__points">1</span></div><div class="tile">Y<span class="tile__points">4</span></div></div>
    <div class="tile-column tile-column--low"><div class="tile">A<span class="tile__points">1</span></div><div class="tile">K<span class="tile__points">5</span></div><div class="tile">U<span class="tile__points">1</span></div><div class="tile">E<span class="tile__points">1</span></div><div class="tile">O<span class="tile__points">1</span></div><div class="tile">Y<span class="tile__points">4</span></div></div>
    <div class="tile-column"><div class="tile">A<span class="tile__points">1</span></div><div class="tile">K<span class="tile__points">5</span></div><div class="tile">U<span class="tile__points">1</span></div><div class="tile">E<span class="tile__points">1</span></div><div class="tile">O<span class="tile__points">1</span></div><div class="tile">Y<span class="tile__points">4</span></div></div>
    <div class="tile-column tile-column--low"><div class="tile">A<span class="tile__points">1</span></div><div class="tile">K<span class="tile__points">5</span></div><div class="tile">U<span class="tile__points">1</span></div><div class="tile">E<span class="tile__points">1</span></div><div class="tile">O<span class="tile__points">1</span></div><div class="tile">Y<span class="tile__points">4</span></div></div>
    <div class="tile-column"><div class="tile">A<span class="tile__points">1</span></div><div class="tile">K<span class="tile__points">5</span></div><div class="tile">U<span class="tile__points">1</span></div><div class="tile">E<span class="tile__points">1</span></div><div class="tile">O<span class="tile__points">1</span></div><div class="tile">Y<span class="tile__points">4</span></div></div>
    <div class="tile-column tile-column--low"><div class="tile">A<span class="tile__points">1</span></div><div class="tile">K<span class="tile__points">5</span></div><div class="tile">U<span class="tile__points">1</span></div><div class="tile">E<span class="tile__points">1</span></div><div class="tile">O<span class="tile__points">1</span></div><div class="tile">Y<span class="tile__points">4</span></div></div>
    <div class="tile-column"><div class="tile">A<span class="tile__points">1</span></div><div class="tile">K<span class="tile__points">5</span></div><div class="tile">U<span class="tile__points">1</span></div><div class="tile">E<span class="tile__points">1</span></div><div class="tile">O<span class="tile__points">1</span></div><div class="tile">Y<span class="tile__points">4</span></div></div>
  </main>

  <aside class="side-panel">
    <div class="stat stat--score">Score: 150</div>
    <div class="stat stat--word">CURRENT WORD</div>
    <div class="stat stat--points">10 POINTS</div>
    <div class="stat stat--level">LEVEL 1</div>
    <div class="action action--clear">CLEAR</div>
    <div class="action action--scramble">SCRAMBLE</div>
    <div class="action action--submit">SUBMIT</div>
  </aside>
</body>
</html>
```